Brightvale Leaf is a bridge for the people who drink tea to connect with the people who make the tea and the environment in which it is grown.

As a start-up, Brightvale Leaf needs to establish a fluently persuasive brand image that articulates its unique mission to the up-market tea drinker.

Our passion for high quality tea and our respect for people are boundless. But our budget is shoe-string. Still, we will allocate a disproportionate amount to evolving a brand; including logo, labeling, and packaging, and hope this initial effort will lead to a long-term relationship with a designer. The Brightvale label, as a component of the brand, must deny the commodity image of tea by broadcasting the uniquely flavorful, healthful, and relaxing experience of drinking tea.

The logo is an image of a liquor pouring from above into a stylized outline of a cup and gracefully folding over on itself within the cup. The image is an echo of video clips that will be featured on the Product page of the ecommerce site. Our initial thought is for the liquor and cup to be white on a rich blue background. But you may have a better idea.

The label must fit a seamless tin canister 4" in diameter; 2" high with a "window" in the lid. There are really three distinct parts to the label: a) wrap-around for the body of the tin; b) a distinct piece to be applied underneath the tin; and c) security strip (s) that connect the lid and the bottom of the tin. The wrap-around must include the following components: the logo, the brand name 'Brightvale Leaf', the name of the specific tea and space for the following characteristics of the tea: Tea / Garden Name, Harvest Date, Tasting Notes, Weight, Location, and Caffeine content. The piece to be affixed underneath the tin should accommodate Ingredients, Brewing Instructions, and contact details for Brightvale Leaf. The security strip(s) should be an integral part of the overall visual.

The color scheme should be expandable, i.e.; different colors for different teas.
We are thinking about rich and bold colors. But am eager to see what inspires you!

A very rough proto-type is captured in the attached files.

Target Market(s)

Ages 25 to 45 in densely populated areas of the U.S. and Canada will an above average house-hold income and an interest in what they eat / drink.

Industry/Entity Type

Environment

Requirements
Must have
• 1. Three separate pieces: 1) wrap around for the body of the tin; 2) piece to be affixed to the bottom of the body of the tin; 3) security strip (s). A word about strips: am unsure about one vs two because, two will add to overhead and processing while one will block the view of the contents. Maybe you know how to resolve.
2. clean, crisp lines
3. uncluttered
Nice to have
• 1. a color scheme to accommodate up to 30 different teas. Do not fall into the trap of incorporating the color green on the label for a 'green tea' and yellow for a lemon flavored tea. That approach is limited and has been overdone.
2. a color scheme that, as it expands to accommodate 30 teas, also is anchored by a brand color set. In other words, all labels include a recognizable color set.
3. express the level of caffeine via a gauge or metric
Should not have
• photo images,

```html
<!DOCTYPE html>
<html lang="en">
<head>
<meta charset="utf-8">
<title>Brightvale Leaf – Tin Label Concepts</title>
<link rel="stylesheet" href="https://fonts.googleapis.com/css2?family=Handlee&family=Great+Vibes&family=Lato:wght@300;400&display=swap">
<style>
  :root{
    --canvas:#ffffff;
    --navy:#1f2560;
    --royal:#2b3990;
    --frame:#c9c9c9;
    --label-grey:#8b8fb0;
    --script-grey:#7d80a6;
    --soft-white:#e8e8f2;
    --gold:#b8854a;
    --cream:#f3e6d2;
  }
  html,body{margin:0;padding:0;width:1200px;height:829px;overflow:hidden;background:var(--canvas);}
  .concept-sheet{display:block;width:1200px;height:829px;}
  .label-frame{fill:var(--canvas);stroke:var(--frame);stroke-width:1.2;}
  .navy-field{fill:var(--navy);}
  .royal-field{fill:var(--royal);}
  .strip-light{fill:var(--canvas);stroke:var(--frame);stroke-width:1.2;}
  .strip-royal{fill:var(--royal);}
  .logo-diamond{fill:var(--canvas);stroke:var(--navy);stroke-width:3;}
  .logo-diamond--royal{stroke:var(--royal);}
  .hand{font-family:"Handlee",cursive;fill:var(--script-grey);}
  .hand--small{font-size:10px;}
  .hand--brand{font-size:30px;}
  .hand--light{fill:var(--soft-white);}
  .clean{font-family:"Lato",sans-serif;font-weight:300;font-size:11px;fill:var(--label-grey);}
  .clean--white{fill:#ffffff;}
  .clean--name{font-size:22px;fill:#a4a6c0;}
  .script-brand{font-family:"Great Vibes",cursive;font-size:28px;fill:var(--royal);}
  .script-strip{font-family:"Great Vibes",cursive;font-size:19px;fill:#ffffff;}
  .script-vertical{font-family:"Great Vibes",cursive;font-size:16px;fill:var(--royal);}
  .gauge-white{fill:#ffffff;}
  .gauge-navy{fill:var(--navy);}
  .gauge-royal{fill:var(--royal);}
  .gauge-outline{fill:none;stroke:#ffffff;stroke-width:1;}
</style>
</head>
<body>
<svg class="concept-sheet" viewBox="0 0 1200 829" xmlns="http://www.w3.org/2000/svg">
  <defs>
    <linearGradient id="goldWave" x1="0" y1="0" x2="1" y2="0">
      <stop offset="0" stop-color="#b8854a"/>
      <stop offset="0.35" stop-color="#f3e6d2"/>
      <stop offset="0.65" stop-color="#c9995e"/>
      <stop offset="1" stop-color="#e9d4b4"/>
    </linearGradient>
    <linearGradient id="pourArt" x1="0" y1="0" x2="0" y2="1">
      <stop offset="0" stop-color="#e2c49a"/>
      <stop offset="1" stop-color="#d7d7dc"/>
    </linearGradient>
    <linearGradient id="cupsArt" x1="0" y1="0" x2="0" y2="1">
      <stop offset="0" stop-color="#ecd7b6"/>
      <stop offset="1" stop-color="#f6f1ea"/>
    </linearGradient>
  </defs>

  <!-- Concept A: wave wrap, name on strip -->
  <g class="concept concept--wave-a">
    <rect class="strip-light" x="329" y="17" width="38" height="165"/>
    <text class="hand" font-size="20" transform="translate(341,28) rotate(90)">name of tea</text>
    <rect class="label-frame" x="85" y="181" width="526" height="198"/>
    <path class="navy-field" d="M85 300 C200 330 300 280 400 300 C480 315 540 262 611 252 V378.4 H85.6 Z"/>
    <path role="img" aria-label="Flowing gold tea wave with glistening bubbles" fill="url(#goldWave)" opacity="0.9"
      d="M85 226 C180 232 260 290 360 282 C450 276 530 236 611 230 V262 C540 268 470 318 390 312 C290 304 190 330 85 304 Z"/>
    <text class="hand hand--small" x="106" y="200">weight</text>
    <text class="hand hand--small" x="106" y="232">growing region</text>
    <text class="hand hand--small" x="424" y="202">harvest date</text>
    <text class="hand hand--small" x="424" y="230">tasting notes</text>
    <rect class="logo-diamond" x="293" y="217" width="96" height="96" transform="rotate(45 341 265)"/>
    <rect role="img" aria-label="Tea pouring into a white cup" x="312" y="226" width="58" height="52" rx="6" fill="url(#pourArt)"/>
    <text class="hand hand--brand hand--light" x="347" y="348" text-anchor="middle">brightvale</text>
    <text class="hand hand--brand hand--light" x="347" y="371" text-anchor="middle">leaf</text>
    <text class="hand hand--small hand--light" x="533" y="340">caffeine level</text>
    <g class="caffeine-gauge">
      <rect class="gauge-white" x="498" y="350" width="8" height="8" transform="rotate(45 502 354)"/>
      <rect class="gauge-white" x="514" y="350" width="8" height="8" transform="rotate(45 518 354)"/>
      <rect class="gauge-white" x="530" y="350" width="8" height="8" transform="rotate(45 534 354)"/>
      <rect class="gauge-white" x="546" y="350" width="8" height="8" transform="rotate(45 550 354)"/>
      <rect class="gauge-white" x="562" y="350" width="8" height="8" transform="rotate(45 566 354)"/>
    </g>
  </g>

  <!-- Concept B: royal curve, name on strip -->
  <g class="concept concept--curve-a">
    <rect class="strip-royal" x="890" y="17" width="37" height="165"/>
    <text class="script-strip" transform="translate(902,64) rotate(90)">name of tea</text>
    <rect class="label-frame" x="645" y="181" width="526" height="198"/>
    <path class="royal-field" d="M645 181 H1171 V292 C1100 300 1010 240 910 216 C810 196 720 226 645 254 Z"/>
    <rect class="logo-diamond logo-diamond--royal" x="858" y="213" width="100" height="100" transform="rotate(45 908 263)"/>
    <rect role="img" aria-label="Two tea cups with pouring tea" x="830" y="215" width="160" height="80" rx="14" fill="url(#cupsArt)"/>
    <text class="clean" x="655" y="270">Harvest Date</text>
    <text class="clean" x="655" y="301">Tasting Notes</text>
    <text class="clean" x="655" y="332">Weight</text>
    <text class="clean" x="655" y="363">Growing Region</text>
    <text class="script-brand" x="905" y="358" text-anchor="middle">Brightvale Leaf</text>
    <text class="script-vertical" transform="translate(1128,362) rotate(-90)">Caffeine Level</text>
    <g class="caffeine-gauge">
      <rect class="gauge-royal" x="1138" y="272" width="10" height="10" transform="rotate(45 1143 277)"/>
      <rect class="gauge-royal" x="1138" y="294" width="10" height="10" transform="rotate(45 1143 299)"/>
      <rect class="gauge-royal" x="1138" y="316" width="10" height="10" transform="rotate(45 1143 321)"/>
      <rect class="gauge-royal" x="1138" y="338" width="10" height="10" transform="rotate(45 1143 343)"/>
      <rect class="gauge-royal" x="1138" y="360" width="10" height="10" transform="rotate(45 1143 365)"/>
    </g>
  </g>

  <!-- Concept C: wave wrap, gauge on strip -->
  <g class="concept concept--wave-b">
    <rect class="strip-light" x="329" y="422" width="38" height="166"/>
    <text class="hand" font-size="6" transform="translate(336,512) rotate(90)">caffeine level</text>
    <g class="caffeine-gauge">
      <rect class="gauge-navy" x="348" y="483" width="9" height="9" transform="rotate(45 352.5 487.5)"/>
      <rect class="gauge-navy" x="348" y="499" width="9" height="9" transform="rotate(45 352.5 503.5)"/>
      <rect class="gauge-navy" x="348" y="515" width="9" height="9" transform="rotate(45 352.5 519.5)"/>
      <rect class="gauge-navy" x="348" y="531" width="9" height="9" transform="rotate(45 352.5 535.5)"/>
      <rect class="gauge-navy" x="348" y="547" width="9" height="9" transform="rotate(45 352.5 551.5)"/>
    </g>
    <rect class="label-frame" x="85" y="587" width="526" height="197"/>
    <path class="navy-field" d="M85 690 C200 720 300 672 400 690 C480 704 540 652 611 642 V783.4 H85.6 Z"/>
    <path role="img" aria-label="Flowing gold tea wave with glistening bubbles" fill="url(#goldWave)" opacity="0.9"
      d="M85 630 C180 636 260 690 360 682 C450 676 530 636 611 630 V660 C540 666 470 712 390 706 C290 698 190 722 85 700 Z"/>
    <rect class="logo-diamond" x="293" y="599" width="96" height="96" transform="rotate(45 341 647)"/>
    <rect role="img" aria-label="Tea pouring into a white cup" x="312" y="608" width="58" height="52" rx="6" fill="url(#pourArt)"/>
    <text class="hand" font-size="26" x="183" y="620" text-anchor="middle">brightvale</text>
    <text class="hand" font-size="26" x="183" y="644" text-anchor="middle">leaf</text>
    <text class="hand" font-size="26" x="508" y="621" text-anchor="middle">name of tea</text>
    <text class="hand hand--small hand--light" x="318" y="742">weight</text>
    <text class="hand hand--small hand--light" x="475" y="742">harvest date</text>
    <text class="hand hand--small hand--light" x="318" y="774">growing region</text>
    <text class="hand hand--small hand--light" x="475" y="774">tasting notes</text>
  </g>

  <!-- Concept D: royal curve, gauge on strip -->
  <g class="concept concept--curve-b">
    <rect class="strip-royal" x="889" y="422" width="37" height="166"/>
    <text class="clean clean--white" transform="translate(904,556) rotate(-90)">Caffeine Level</text>
    <g class="caffeine-gauge">
      <rect class="gauge-outline" x="912" y="484" width="8" height="8" transform="rotate(45 916 488)"/>
      <rect class="gauge-outline" x="912" y="500" width="8" height="8" transform="rotate(45 916 504)"/>
      <rect class="gauge-outline" x="912" y="516" width="8" height="8" transform="rotate(45 916 520)"/>
      <rect class="gauge-outline" x="912" y="532" width="8" height="8" transform="rotate(45 916 536)"/>
      <rect class="gauge-outline" x="912" y="548" width="8" height="8" transform="rotate(45 916 552)"/>
    </g>
    <rect class="label-frame" x="645" y="587" width="526" height="197"/>
    <path class="royal-field" d="M645 587 H1171 V698 C1100 706 1010 646 910 622 C810 602 720 632 645 660 Z"/>
    <rect class="logo-diamond logo-diamond--royal" x="857" y="598" width="100" height="100" transform="rotate(45 907 648)"/>
    <rect role="img" aria-label="Two tea cups with pouring tea" x="829" y="600" width="160" height="80" rx="14" fill="url(#cupsArt)"/>
    <text class="clean" x="655" y="721">Harvest Date</text>
    <text class="clean" x="655" y="752">Tasting Notes</text>
    <text class="clean" x="1063" y="721">Weight</text>
    <text class="clean" x="1063" y="752">Growing Region</text>
    <text class="script-brand" x="905" y="745" text-anchor="middle">Brightvale Leaf</text>
    <text class="clean clean--name" x="907" y="775" text-anchor="middle">name of tea</text>
  </g>
</svg>
</body>
</html>
```